I need a business card for myself, being a proprietor of a funeral parlor based in Manila. I'd like the card to have either of the following:
White Font on Black Background
or
Black Font on White Background
No logo is needed however I will appreciate any efforts to show a symbol of eternal happiness, aptly designed with above mentioned colors in mind.
Company name, address and contact on the lower right corner.
Logo or symbol anywhere.
Brightvale Funeral Services
+639174412870
dariel4412@quillmail.com
corner of Corvina Avenue and Halberd Street
Makati City, Philippines
Thank you.
Update: Please include a small dove in your design. You are free to choose where you would like it on the card.

```html
<!DOCTYPE html>
<html lang="en">
<head>
<meta charset="utf-8">
<title>Brightvale Funeral Services – Business Cards</title>
<link rel="stylesheet" href="https://fonts.googleapis.com/css2?family=Lato:wght@400;700&display=swap">
<style>
  :root {
    --stage: #e6e3df;
    --paper: #f7f7f7;
    --ink: #1a1a1a;
    --night: #0b0b0b;
    --snow: #ffffff;
    --grey: #8a8a8a;
  }
  * { margin: 0; padding: 0; box-sizing: border-box; }
  html, body { width: 1200px; height: 1023px; overflow: hidden; }
  body {
    background: var(--stage);
    font-family: 'Lato', sans-serif;
    display: flex;
    align-items: center;
    justify-content: center;
    gap: 80px;
  }
  .card {
    width: 400px;
    height: 660px;
    display: flex;
    flex-direction: column;
    align-items: center;
    padding-top: 70px;
    text-align: center;
    box-shadow: 0 12px 30px rgba(0,0,0,0.18);
  }
  .card--light { background: var(--paper); color: var(--ink); --accent: var(--ink); --icon-fg: var(--snow); }
  .card--dark { background: var(--night); color: var(--snow); --accent: var(--snow); --icon-fg: var(--night); }
  .brand {
    display: flex;
    align-items: center;
    gap: 12px;
    margin-bottom: 48px;
  }
  .brand__dot {
    width: 34px; height: 34px;
    border-radius: 50%;
    background: var(--accent);
  }
  .brand__name {
    font-size: 34px;
    font-weight: 700;
    color: var(--accent);
  }
  .company {
    font-size: 22px;
    font-weight: 400;
    margin-bottom: 70px;
  }
  .contact { display: flex; flex-direction: column; align-items: center; }
  .contact__icon {
    width: 28px; height: 28px;
    margin-bottom: 10px;
  }
  .contact__text {
    font-size: 19px;
    line-height: 1.3;
    margin-bottom: 18px;
  }
</style>
</head>
<body>

<section class="card card--light">
  <div class="brand"><span class="brand__dot"></span><span class="brand__name">Brightvale</span></div>
  <p class="company">Brightvale Funeral Services</p>
  <div class="contact">
    <svg class="contact__icon" viewBox="0 0 28 28"><circle cx="14" cy="14" r="13" fill="var(--accent)"/><path d="M7 14 L14 8 L21 14 M9 13 V20 H19 V13" fill="none" stroke="var(--icon-fg)" stroke-width="1.8"/></svg>
    <p class="contact__text">Corner of Corvina Avenue,<br>and Halberd Street<br>Makati City, Philippines.</p>
    <svg class="contact__icon" viewBox="0 0 28 28"><circle cx="14" cy="14" r="13" fill="var(--accent)"/><path d="M8 11 Q14 6 20 11 L18 13 H10 Z M10 14 H18 V20 H10 Z" fill="var(--icon-fg)"/></svg>
    <p class="contact__text">+639174412870</p>
    <svg class="contact__icon" viewBox="0 0 28 28"><circle cx="14" cy="14" r="13" fill="var(--accent)"/><rect x="7.5" y="9.5" width="13" height="9" fill="none" stroke="var(--icon-fg)" stroke-width="1.6"/><path d="M7.5 9.5 L14 15 L20.5 9.5" fill="none" stroke="var(--icon-fg)" stroke-width="1.6"/></svg>
    <p class="contact__text">dariel4412@quillmail.com</p>
  </div>
</section>

<section class="card card--dark">
  <div class="brand"><span class="brand__dot"></span><span class="brand__name">Brightvale</span></div>
  <p class="company">Brightvale Funeral Services</p>
  <div class="contact">
    <svg class="contact__icon" viewBox="0 0 28 28"><circle cx="14" cy="14" r="13" fill="var(--accent)"/><path d="M7 14 L14 8 L21 14 M9 13 V20 H19 V13" fill="none" stroke="var(--icon-fg)" stroke-width="1.8"/></svg>
    <p class="contact__text">Corner of Corvina Avenue,<br>and Halberd Street<br>Makati City, Philippines.</p>
    <svg class="contact__icon" viewBox="0 0 28 28"><circle cx="14" cy="14" r="13" fill="var(--accent)"/><path d="M8 11 Q14 6 20 11 L18 13 H10 Z M10 14 H18 V20 H10 Z" fill="var(--icon-fg)"/></svg>
    <p class="contact__text">+639174412870</p>
    <svg class="contact__icon" viewBox="0 0 28 28"><circle cx="14" cy="14" r="13" fill="var(--accent)"/><rect x="7.5" y="9.5" width="13" height="9" fill="none" stroke="var(--icon-fg)" stroke-width="1.6"/><path d="M7.5 9.5 L14 15 L20.5 9.5" fill="none" stroke="var(--icon-fg)" stroke-width="1.6"/></svg>
    <p class="contact__text">dariel4412@quillmail.com</p>
  </div>
</section>

</body>
</html>
```